Lagoonworks Solutions

I run an aquarium service business covering all aspects of large scale saltwater aquariums. Design, installation, and service. My main customer base is corporations in Manhattan, but I also deal with smaller home or business aquariums in the tri-state area. I work with cutting edge equipment and service techniques and need to convey that.

Industry/Entity Type

Business

Contact Information for Business Card

LAGOONWORKS SOLUTIONS LLC
Jonathan R. Delvoy
Owner
Main 415-555-0182
Cell 415-555-0267
Service.LagoonSolutions@mailbeam.net

```html
<!DOCTYPE html>
<html lang="en">
<head>
<meta charset="utf-8">
<title>Lagoonworks Solutions – Business Card</title>
<link rel="stylesheet" href="https://fonts.googleapis.com/css2?family=Open+Sans:wght@400;600;700&display=swap">
<style>
  :root {
    --page-bg: #e9ecee;
    --card-edge: #d6e6ea;
    --card-top: #f4f9fb;
    --card-mid: #ffffff;
    --card-tint: #cfe7ee;
    --brand-blue: #2aa6e0;
    --ink: #1f2326;
    --metal-dark: #5b6670;
    --metal-light: #c9d2d8;
  }
  * { margin: 0; padding: 0; box-sizing: border-box; }
  html, body {
    width: 1200px;
    height: 1023px;
    overflow: hidden;
    background: var(--page-bg);
    font-family: "Open Sans", Arial, sans-serif;
  }
  .canvas {
    position: relative;
    width: 1200px;
    height: 1023px;
  }
  .business-card {
    position: absolute;
    left: 180px;
    top: 272px;
    width: 840px;
    height: 480px;
    border: 1px solid var(--card-edge);
    background:
      radial-gradient(ellipse at 55% 45%, var(--card-mid) 0%, var(--card-top) 55%, var(--card-tint) 100%);
    box-shadow: 0 6px 18px rgba(0, 0, 0, 0.18);
    overflow: hidden;
  }
  .seahorse-art {
    position: absolute;
    left: 18px;
    top: 150px;
    width: 320px;
    height: 320px;
    border-radius: 40% 45% 30% 50%;
    background: radial-gradient(ellipse at 45% 50%, var(--metal-light) 0%, #8f9aa3 45%, var(--metal-dark) 75%, rgba(91, 102, 112, 0) 100%);
  }
  .seahorse-watermark {
    position: absolute;
    left: 520px;
    top: 10px;
    width: 300px;
    height: 290px;
    border-radius: 45%;
    background: radial-gradient(ellipse at 50% 50%, rgba(150, 165, 175, 0.28) 0%, rgba(150, 165, 175, 0.12) 55%, rgba(150, 165, 175, 0) 80%);
  }
  .company-name {
    position: absolute;
    left: 300px;
    top: 46px;
    font-size: 30px;
    font-weight: 700;
    color: var(--brand-blue);
    letter-spacing: 0.2px;
  }
  .person-name {
    position: absolute;
    left: 362px;
    top: 168px;
    font-size: 30px;
    font-weight: 600;
    color: var(--brand-blue);
  }
  .person-role {
    position: absolute;
    left: 384px;
    top: 212px;
    font-size: 20px;
    color: var(--ink);
  }
  .contact-list {
    position: absolute;
    left: 392px;
    top: 284px;
    list-style: none;
  }
  .contact-item {
    display: flex;
    align-items: center;
    gap: 12px;
    height: 36px;
    font-size: 20px;
    color: var(--ink);
  }
  .contact-icon {
    width: 16px;
    height: 20px;
    flex: none;
  }
  .contact-label {
    display: inline-block;
    width: 48px;
  }
</style>
</head>
<body>
<main class="canvas">
  <section class="business-card">
    <div class="seahorse-watermark" role="img" aria-label="Faint mechanical seahorse illustration in the background"></div>
    <div class="seahorse-art" role="img" aria-label="Mechanical seahorse illustration built from metal parts, with small bubbles"></div>

    <h1 class="company-name">LAGOONWORKS SOLUTIONS LLC</h1>
    <h2 class="person-name">Jonathan R. Delvoy</h2>
    <p class="person-role">Owner</p>

    <ul class="contact-list">
      <li class="contact-item">
        <svg class="contact-icon" viewBox="0 0 16 20" aria-hidden="true">
          <rect x="2" y="1" width="12" height="18" rx="2" fill="none" stroke="#1f2326" stroke-width="2"/>
          <line x1="6" y1="16" x2="10" y2="16" stroke="#1f2326" stroke-width="1.5"/>
        </svg>
        <span><span class="contact-label">Main</span>415-555-0182</span>
      </li>
      <li class="contact-item">
        <svg class="contact-icon" viewBox="0 0 16 20" aria-hidden="true">
          <rect x="2" y="1" width="12" height="18" rx="2" fill="none" stroke="#1f2326" stroke-width="2"/>
          <line x1="6" y1="16" x2="10" y2="16" stroke="#1f2326" stroke-width="1.5"/>
        </svg>
        <span><span class="contact-label">Cell</span>415-555-0267</span>
      </li>
      <li class="contact-item">
        <svg class="contact-icon" viewBox="0 0 16 20" aria-hidden="true">
          <rect x="1" y="5" width="14" height="11" fill="#1f2326"/>
          <polyline points="1,5 8,11 15,5" fill="none" stroke="#ffffff" stroke-width="1.5"/>
        </svg>
        <span>Service.LagoonSolutions@mailbeam.net</span>
      </li>
    </ul>
  </section>
</main>
</body>
</html>
```